Business Card Design

About Us
VaultNetix is a young and innovative company focusing on security and hosting solutions for global enterprise. To supply the high-performance, highly interconnected and low latency DDoS protection service, we distributed a large number of huge scrubbing centers all over the world. So VaultNetix is the first choice for enterprise to protect their network security.

Task detail
1. We hope that the business card can be filled with creativity, simple and technologe, the business card background is white, the business card text color and other colors are black, blue, green or your needs.

2. We need the source files provided by the successful bidder, such as *.psd, *.ai, etc.

3. One side contains the following:
-Logo
-Brin Sales Manager
-VAULTNETIX TECHNOLOGY CO., LIMITED
-Add:
9/F., Harmon Tower,
218 Pellow Street, Tai Hang, Kowloon,
HK
-Tel: 86-755-4172 0583
-Phone: 86-189 6041 3725
-Email: brin@vault-netix.com
-Web: www.vault-netix.com

4. The other side contains the following:
-Logo

5. Please find the attachment contains the logo PSD source files.

```html
<!DOCTYPE html>
<html lang="en">
<head>
<meta charset="utf-8">
<title>VaultNetix Business Card</title>
<link href="https://fonts.googleapis.com/css2?family=Open+Sans:wght@400;600;700&display=swap" rel="stylesheet">
<style>
  :root {
    --stage: #4b4c4e;
    --teal: #2eb1c6;
    --teal-light: #35b8cc;
    --teal-dark: #28a9bd;
    --green: #6cc04a;
    --ink: #3a3a3a;
    --white: #ffffff;
  }
  * { margin: 0; padding: 0; box-sizing: border-box; }
  html, body { width: 1200px; height: 1000px; overflow: hidden; }
  body {
    background: var(--stage);
    font-family: "Open Sans", Arial, sans-serif;
    position: relative;
  }
  .card {
    position: absolute;
    box-shadow: 0 6px 18px rgba(0,0,0,0.35);
  }
  .card-front {
    left: 158px; top: 173px; width: 526px; height: 307px;
    background: var(--teal);
  }
  .card-back {
    left: 510px; top: 533px; width: 523px; height: 305px;
    background: var(--white);
  }
  .brand {
    position: absolute;
    display: flex; align-items: center; gap: 12px;
    font-weight: 700; line-height: 1; white-space: nowrap;
  }
  .brand-mark { display: block; flex: none; }

  .card-front .brand { left: 109px; top: 122px; font-size: 52px; color: var(--white); }
  .card-front .brand-mark { width: 40px; height: 40px; background: var(--white); }

  .card-back .brand { left: 27px; top: 62px; font-size: 38px; color: var(--ink); }
  .card-back .brand-mark { width: 30px; height: 30px; background: var(--teal); }

  .brick-band {
    position: absolute; left: 0; width: 100%; height: 27px;
    background: linear-gradient(180deg, var(--teal-light), var(--teal-dark));
  }
  .brick-band.top { top: 0; }
  .brick-band.bottom { bottom: 0; }

  .person {
    position: absolute; right: 34px; top: 122px; text-align: right;
  }
  .person-name { font-size: 20px; font-weight: 700; color: var(--green); line-height: 1.1; }
  .person-role { font-size: 12.5px; color: var(--ink); margin-top: 2px; }

  .divider {
    position: absolute; left: 27px; right: 33px; top: 167px;
    height: 2px; background: var(--teal);
  }

  .company {
    position: absolute; left: 27px; top: 197px;
    font-size: 12.5px; line-height: 17px; color: var(--ink); font-style: normal;
  }
  .company-name { font-weight: 700; color: var(--green); }

  .contacts {
    position: absolute; right: 33px; top: 192px;
    list-style: none; font-size: 12.5px; color: var(--ink);
  }
  .contacts li {
    display: flex; align-items: center; justify-content: flex-end;
    gap: 8px; height: 17.5px;
  }
  .contacts svg { width: 13px; height: 13px; fill: none; stroke: var(--green); stroke-width: 1.8; flex: none; }
  .contacts svg .solid { fill: var(--green); stroke: none; }
</style>
</head>
<body>

  <section class="card card-front" aria-label="Card front">
    <div class="brand"><span class="brand-mark"></span>VaultNetix</div>
  </section>

  <section class="card card-back" aria-label="Card back">
    <div class="brick-band top" role="img" aria-label="Teal brick wall pattern band"></div>

    <div class="brand"><span class="brand-mark"></span>VaultNetix</div>

    <div class="person">
      <div class="person-name">Brin</div>
      <div class="person-role">Sales Manager</div>
    </div>

    <div class="divider"></div>

    <address class="company">
      <div class="company-name">VaultNetix</div>
      <div>9/F, Harmon Tower,</div>
      <div>218 Pellow Street,</div>
      <div>Tai Hang, Kowloon, HK</div>
    </address>

    <ul class="contacts">
      <li>86-755-4172 0583
        <svg viewBox="0 0 16 16"><path d="M4 1.5l2.5 3-1.5 1.8c.8 1.8 2.3 3.3 4.1 4.2l1.8-1.5 3 2.5-1.6 2.6C7 13.6 2.4 9 1.9 3.2z"/></svg>
      </li>
      <li>86-189 6041 3725
        <svg viewBox="0 0 16 16"><rect x="4.5" y="1" width="7" height="14" rx="1.2"/><circle class="solid" cx="8" cy="12.5" r="0.9"/></svg>
      </li>
      <li>brin@vault-netix.com
        <svg viewBox="0 0 16 16"><rect class="solid" x="1" y="3.5" width="14" height="9"/><path d="M1.5 4l6.5 5 6.5-5" stroke="#fff"/></svg>
      </li>
      <li>www.vault-netix.com
        <svg viewBox="0 0 16 16"><circle cx="8" cy="8" r="6.5"/><path d="M1.5 8h13M8 1.5c-2.5 3-2.5 10 0 13M8 1.5c2.5 3 2.5 10 0 13"/></svg>
      </li>
    </ul>

    <div class="brick-band bottom" role="img" aria-label="Teal brick wall pattern band"></div>
  </section>

</body>
</html>
```